Ridecraft Academy Wordpress Motorcycle School Business Website

We are a motorcycle training school that is located in Calgary, AB, Canada. Our main service is motorcycle safety training. We currently have a site at www.ridecraftacademy.example . We would like to see a design whereby the colours align with our logo (a white background is best), as well as effectively communicating our strengths as a school and the value and quality of the services we provide.

There are also photos on our facebook page at: www.facebook.com/ridecraftacademy/ , it would be nice to incorporate some, but we are open to using generic photos as well.

It is important that the entire site be mobile friendly. The front page should be able to house all the information that a potential student would be looking for in terms of WHY they should choose us, without having to navigate to secondary pages.

We also currently have a small youtube clip that we would like to keep on the main page to "hook" a potential customer. We have secondary pages in our menu for further details and also have an integrated booking engine on one of the pages so that student's can book and pay online. These things we would like to keep. It would also be nice to give the ability for our customers to share the website's pages on social media.

Our current subpages are:
About Us
Our Staff
Our Fleet
Client Testimonials
Friends of Ridecraft
Course Descriptions
Course Pricing
Bookings (where they book)
FAQ
Privacy Policy
Contact Page

A more efficient and effective method of organizing/delivering the content would be great.

Finally... a sleek, modern/contemporary theme is what we are after. Our company slogan being: Fun - Safe - Professional

Please reference the existing website for all the necessary content.

Target Market(s)

18-50 year old. Motorcycle enthusiast students who want to learn to ride.

Industry/Entity Type

Driving School

Font styles to use
Sans Serif

Requirements
Must have
• Some photos from our facebook page would be great.
• Ridecraft Academy Logo colours
• Please refer to the Project Description.
Nice to have
• Modern/Contemporary

```html
<!DOCTYPE html>
<html lang="en">
<head>
<meta charset="utf-8">
<title>Ridecraft Academy</title>
<link rel="stylesheet" href="https://fonts.googleapis.com/css2?family=Open+Sans:wght@400;600;700&family=Oswald:wght@400;500;600&display=swap">
<style>
:root{
  --yellow:#f3c316;
  --yellow-dark:#d9a90a;
  --ink:#2e2e2e;
  --text:#555;
  --muted:#8a8a8a;
  --dark:#343434;
  --darker:#262626;
  --line:#dcdcdc;
  --red:#c8281e;
  --white:#fff;
}
*{box-sizing:border-box;margin:0;padding:0}
html,body{width:1200px;height:2880px;overflow:hidden}
body{font-family:"Open Sans",Arial,sans-serif;color:var(--text);background:var(--white);font-size:14px;line-height:1.6}
.page{position:relative;width:1200px;height:2880px;overflow:hidden}
h2,h3,.nav,.slogan,.btn,.cta-title{font-family:"Oswald","Arial Narrow",sans-serif}
.wrap{width:1080px;margin:0 auto;position:relative}

/* hero */
.hero{position:relative;height:700px}
.hero-photo{position:absolute;inset:0;background:linear-gradient(180deg,#8fa3b8 0%,#b8c4cc 28%,#7f8f5e 50%,#5b6b3c 75%,#3d4530 100%)}
.topbar{position:absolute;top:0;left:0;right:0;height:110px;background:rgba(255,255,255,.93)}
.brand{position:absolute;left:60px;top:26px;display:flex;align-items:center;gap:12px}
.brand-dot{width:18px;height:18px;border-radius:50%;background:var(--red)}
.brand-name{font-family:"Open Sans",Arial,sans-serif;font-weight:700;font-size:30px;color:var(--ink);letter-spacing:.5px}
.social{position:absolute;left:490px;top:16px;display:flex;gap:10px}
.social span{width:26px;height:26px;border-radius:50%;background:var(--dark)}
.contact-top{position:absolute;right:60px;top:18px;display:flex;gap:28px;font-size:13px;color:var(--ink)}
.contact-top span{display:flex;align-items:center;gap:6px}
.nav{position:absolute;right:60px;top:66px;display:flex;gap:34px;font-size:16px;letter-spacing:1px;color:var(--ink)}
.nav a{color:inherit;text-decoration:none}
.nav a:first-child{color:var(--yellow-dark)}
.slogan-band{position:absolute;left:0;right:0;top:600px;height:64px;background:rgba(0,0,0,.55);display:flex;align-items:center;justify-content:center}
.slogan{color:var(--yellow);font-size:34px;letter-spacing:3px}
.dots{position:absolute;right:60px;top:624px;display:flex;gap:8px}
.dots i{width:12px;height:12px;border-radius:50%;background:rgba(255,255,255,.6)}
.dots i:first-child{background:var(--white)}

/* welcome */
.welcome{padding:50px 0 0;height:400px}
.welcome .wrap{display:flex;gap:60px}
.col{flex:1}
.section-title{font-size:28px;color:var(--ink);font-weight:500;margin-bottom:14px;display:flex;align-items:center;gap:10px}
.section-title .brand-name{font-size:26px}
.col p{font-size:14px;color:var(--text)}
.read-more{display:inline-block;margin-top:16px;font-weight:700;color:var(--ink);font-size:13px;text-decoration:none}
.video{height:270px;background:linear-gradient(180deg,#dfe6ea,#a9b7be);position:relative}
.video-bar{position:absolute;left:0;right:0;bottom:0;height:34px;background:#1f1f1f;display:flex;align-items:center;padding:0 12px;gap:12px}
.video-bar .track{flex:1;height:5px;background:#555;position:relative}
.video-bar .track::before{content:"";position:absolute;left:0;top:0;bottom:0;width:18%;background:var(--red)}

/* course bands */
.band{position:relative;color:#eee;text-align:center}
.band-photo{position:absolute;inset:0;background:linear-gradient(180deg,#545454,#2d2d2d)}
.band-inner{position:relative;padding-top:40px}
.band-title{display:inline-block;background:rgba(0,0,0,.55);padding:10px 90px;font-size:24px;font-weight:500;color:var(--white);margin-bottom:22px;border-top:3px solid var(--yellow)}
.band p{width:900px;margin:0 auto 20px;font-size:14px;color:#e5e5e5}
.btn{display:inline-block;background:var(--yellow);color:var(--ink);font-size:16px;padding:9px 26px;letter-spacing:.5px;text-decoration:none;font-weight:500}
.band.basic{height:260px;margin-top:40px}
.band.pro{height:300px}

/* comparison */
.why{height:460px;padding-top:42px}
.why h2{text-align:center;font-size:30px;color:var(--ink);font-weight:500;margin-bottom:24px}
.compare{width:1080px;margin:0 auto;border-collapse:collapse;font-size:12.5px}
.compare th{background:var(--dark);color:var(--white);text-align:left;padding:7px 10px;font-weight:600;font-size:12px;text-transform:uppercase}
.compare td{border:1px solid var(--line);padding:6px 10px;color:var(--text);vertical-align:top}
.compare td:first-child{width:30%}
.compare td:nth-child(2){width:46%}
.compare tr:nth-child(even) td{background:#f6f6f6}

/* news + testimonials */
.lower{height:360px;padding-top:44px}
.lower .wrap{display:flex;gap:60px}
.lower h2{font-size:26px;font-weight:500;color:var(--ink);margin-bottom:20px}
.news-item{display:flex;gap:16px;margin-bottom:18px}
.news-date{width:56px;height:56px;background:var(--yellow);color:var(--ink);text-align:center;font-family:"Oswald",sans-serif;line-height:1.1;padding-top:8px;flex:none}
.news-date b{display:block;font-size:20px}
.news-item h3{font-family:"Open Sans",sans-serif;font-size:14px;color:var(--ink);font-weight:700}
.news-item p{font-size:12.5px;color:var(--muted)}
.testimonial{display:flex;gap:22px;align-items:flex-start}
.avatar{width:110px;height:110px;border-radius:50%;background:linear-gradient(135deg,#9a9a9a,#5d5d5d);flex:none}
.testimonial p{font-style:italic;font-size:14px}
.testimonial .who{display:block;text-align:right;font-style:normal;font-weight:700;color:var(--ink);margin-top:10px}

/* cta */
.cta{height:100px;background:var(--yellow)}
.cta .wrap{height:100px;display:flex;align-items:center;justify-content:space-between}
.cta-title{font-size:22px;color:var(--ink);font-weight:400;letter-spacing:.5px}
.cta .btn{background:var(--dark);color:var(--white);padding:12px 30px;text-align:center;line-height:1.2}

/* footer */
.footer{height:260px;background:var(--dark);color:#bbb;padding-top:36px}
.footer .wrap{display:flex;gap:70px}
.footer h3{color:var(--white);font-size:17px;font-weight:500;margin-bottom:14px;letter-spacing:.5px}
.footer ul{list-style:none;font-size:13px;line-height:2}
.footer .fcol{width:200px}
.footer .fcol.wide{width:330px}
.footer p{font-size:13px}
.subscribe{display:flex;margin-top:14px}
.subscribe span{width:210px;height:34px;background:#4a4a4a}
.subscribe b{background:var(--yellow);color:var(--ink);font-family:"Oswald",sans-serif;font-weight:500;padding:7px 16px;font-size:14px}
.copyright{height:40px;background:var(--darker);color:#999;font-size:12px;display:flex;align-items:center;padding-left:60px}
</style>
</head>
<body>
<div class="page">

<header class="hero">
  <div class="hero-photo" role="img" aria-label="Photo of instructors in riding gear beside motorcycles on a mountain road"></div>
  <div class="topbar">
    <div class="brand"><span class="brand-dot"></span><span class="brand-name">Ridecraft Academy</span></div>
    <div class="social"><span></span><span></span><span></span></div>
    <div class="contact-top">
      <span><svg width="14" height="12" viewBox="0 0 14 12"><rect x="1" y="1" width="12" height="10" fill="none" stroke="#2e2e2e"/><path d="M1 1l6 5 6-5" fill="none" stroke="#2e2e2e"/></svg>hello@ridecraftacademy.example</span>
      <span><svg width="12" height="14" viewBox="0 0 12 14"><path d="M2 1h3l1 3-2 1.5a7 7 0 0 0 3 3L8.5 7l3 1v3c0 1-1 2-2 2C5 13-1 7 1 3 1 2 1.5 1 2 1z" fill="#2e2e2e"/></svg>(403) 555-0142</span>
    </div>
    <nav class="nav"><a>ABOUT US ▾</a><a>COURSES ▾</a><a>BOOKINGS ▾</a><a>CONTACT</a></nav>
  </div>
  <div class="slogan-band"><span class="slogan">Fun &nbsp;•&nbsp; Safe &nbsp;•&nbsp; Professional</span></div>
  <div class="dots"><i></i><i></i><i></i></div>
</header>

<section class="welcome">
  <div class="wrap">
    <div class="col">
      <h2 class="section-title">Welcome To <span class="brand-name">Ridecraft</span></h2>
      <p>Ridecraft Academy has trained new riders in Calgary for years, giving every student the skills and confidence to ride safely. Our courses pair certified instructors with small class sizes, a large private training lot and a fleet of well kept motorcycles. Whether you are starting out or preparing for your road test, we guide you step by step, from first throttle to open road, with patience and plenty of seat time.</p>
      <a class="read-more">READ MORE ›</a>
    </div>
    <div class="col">
      <h2 class="section-title">Watch Our Video</h2>
      <div class="video" role="img" aria-label="Course introduction video of riders on the training lot">
        <div class="video-bar"><svg width="12" height="14" viewBox="0 0 12 14"><path d="M0 0l12 7-12 7z" fill="#fff"/></svg><div class="track"></div></div>
      </div>
    </div>
  </div>
</section>

<section class="band basic">
  <div class="band-photo" role="img" aria-label="Photo of students practising on motorcycles"></div>
  <div class="band-inner">
    <h2 class="band-title">Ridecraft Basic Motorcycle Training Course</h2>
    <p>Our basic course takes brand new riders from the classroom to the lot, covering controls, balance, braking, cornering and hazard awareness. Students ride our bikes under close supervision and finish ready for the provincial road test with skills that last a lifetime.</p>
    <a class="btn">VIEW OUR CLASS SCHEDULES / BOOK NOW</a>
  </div>
</section>

<section class="why">
  <h2>Why Choose Us? What Makes Us Different From Others?</h2>
  <table class="compare">
    <tr><th>Description</th><th>Ridecraft Academy</th><th>No particular other guys</th></tr>
    <tr><td>Certified by Provincial Transport Board (Qualify for Insurance discount)</td><td>Yes</td><td>No</td></tr>
    <tr><td>Student Instructor Ratio</td><td>4:1</td><td>3:1 – 10:1</td></tr>
    <tr><td>Maximum Lot Class Size</td><td>8</td><td>20</td></tr>
    <tr><td>Training Lot</td><td>Board approved large lot with 2–4 acres</td><td>Smaller</td></tr>
    <tr><td>Classroom Facilities</td><td>Proper classroom with space and equipment</td><td>Improper rooms, offices, halls</td></tr>
    <tr><td>Instructors</td><td>All board licensed, well trained, first aid qualified</td><td>Sometimes uses "Teacher Aids"</td></tr>
    <tr><td>Motorcycles</td><td>Sportbikes and cruisers to pick from, so you are not learning on one bike only</td><td>Same bikes for all courses</td></tr>
    <tr><td>Road Test</td><td>Coordinated and approved for road test with our own bikes</td><td>No help for road tests</td></tr>
  </table>
</section>

<section class="band pro">
  <div class="band-photo" role="img" aria-label="Photo of a rider cornering on an open road"></div>
  <div class="band-inner">
    <h2 class="band-title">Rider Proficiency Training (Advanced Motorcycle Course)</h2>
    <p>Already licensed and want to ride better? This advanced course sharpens braking, swerving, cornering and group riding on both the lot and the street. Experienced instructors give personal coaching so you can enjoy every ride with more control and less risk.</p>
    <a class="btn">VIEW OUR CLASS SCHEDULES / BOOK NOW</a>
  </div>
</section>

<section class="lower">
  <div class="wrap">
    <div class="col">
      <h2>News &amp; Events</h2>
      <div class="news-item"><div class="news-date"><b>14</b>MAR</div><div><h3>Spring course dates now open for booking</h3><p>New weekend and evening classes added for the season ahead.</p></div></div>
      <div class="news-item"><div class="news-date"><b>02</b>APR</div><div><h3>Open house at the training lot</h3><p>Meet our instructors and sit on the bikes before you sign up.</p></div></div>
      <div class="news-item"><div class="news-date"><b>20</b>MAY</div><div><h3>Advanced group ride this summer</h3><p>Graduates are invited to join a guided ride through the foothills.</p></div></div>
    </div>
    <div class="col">
      <h2>Clients Testimonials</h2>
      <div class="testimonial">
        <div class="avatar" role="img" aria-label="Portrait of a past student"></div>
        <p>“The instructors were patient, friendly and clear. I had never ridden before and by the end of the weekend I felt confident and safe. Passed my road test on the first try!”<span class="who">– Dana K.</span></p>
      </div>
    </div>
  </div>
</section>

<section class="cta">
  <div class="wrap">
    <div class="cta-title">WE ARE RIDECRAFT ACADEMY. HAVE QUESTIONS ABOUT OUR CLASSES ?</div>
    <a class="btn">GET IN TOUCH<br>WITH US</a>
  </div>
</section>

<footer class="footer">
  <div class="wrap">
    <div class="fcol">
      <h3>QUICK LINKS</h3>
      <ul><li>› Home</li><li>› About Us</li><li>› Courses</li><li>› Bookings</li><li>› Contact</li></ul>
    </div>
    <div class="fcol wide">
      <h3>CONTACT DETAILS</h3>
      <p>Ridecraft Academy<br>88 Throttle Way SE, Calgary, AB<br>(403) 555-0142<br>hello@ridecraftacademy.example<br>www.ridecraftacademy.example</p>
    </div>
    <div class="fcol wide">
      <h3>NEWSLETTER</h3>
      <p>Subscribe to hear about new course dates and events.</p>
      <div class="subscribe"><span></span><b>SUBSCRIBE</b></div>
    </div>
  </div>
</footer>
<div class="copyright">Copyright © Ridecraft Academy. All rights reserved.</div>

</div>
</body>
</html>
```